Health & Wellness Labels on two Vitamin type bottles.

Hello,

My company is Bright Meadow Vita and I'm looking to get (9) labels done for my health & wellness company as we caring all nature products. I would like all the labels showing an all nature look. I would like my company name at the top of the bottle. I would also like all nature colors such as green,light green and so on. All of the products are Capsules.

Here are all of the different products sizes:
8 Size bottles 200cc and label size 202.00mm X 95.00
1 Size bottle 120cc and label size 169.00mm X 76.00mm

Here are all of the different products:
Tidal Glow Weight Loss ( Size 200 )
Tidal Glow Hair Loss ( Size 200cc )
Tidal Glow Sleeping ( Size 200cc )
Tidal Glow Skin Care ( Size 200cc )
Tidal Glow Energy ( Size 200cc )
Tidal Glow Digestion ( Size 200cc )
Tidal Glow Cold ( Size 200cc )
Tidal Glow Pain ( Size 200CC )
Tidal Glow Cleansing ( Size 120cc )
The tidal glow cleansing is for cleaning out the body.

I have also uploaded my company logo.

```html
<!DOCTYPE html>
<html lang="en">
<head>
<meta charset="utf-8">
<title>Tidal Glow Labels</title>
<link rel="stylesheet" href="https://fonts.googleapis.com/css2?family=Arimo:wght@400;700&family=Open+Sans:wght@400;600&display=swap">
<style>
  :root {
    --page: #ffffff;
    --label-bg: #f4f4f3;
    --olive: #6e7a2c;
    --lime-edge: #b6c233;
    --title-green: #1f6b3b;
    --ink: #1c1c1c;
    --cream: #f5f1e2;
    --band-rule: #9aa0a0;
    --photo-skin: #e6c7ab;
    --photo-light: #eef0ef;
  }
  * { box-sizing: border-box; margin: 0; padding: 0; }
  html, body { width: 1200px; height: 1000px; overflow: hidden; background: var(--page); }
  .canvas { position: relative; width: 1200px; height: 1000px; }

  .label {
    position: absolute; top: 210px; width: 420px; height: 650px;
    background: var(--label-bg); overflow: hidden;
    font-family: "Arimo", Arial, sans-serif; color: var(--ink);
  }
  .label--weight { left: 140px; }
  .label--hair { left: 640px; }

  .label__edges { position: absolute; inset: 0; }

  .maker-name {
    position: absolute; top: 62px; left: 0; width: 100%;
    display: flex; align-items: center; justify-content: center; gap: 8px;
    font-family: "Arimo", Arial, sans-serif; font-weight: 400; font-size: 22px;
    color: var(--olive);
  }
  .maker-name__dot { width: 14px; height: 14px; border-radius: 50%; background: var(--olive); flex: none; }

  .product-mark {
    position: absolute; top: 160px; left: 36px; width: 350px; text-align: center;
    font-weight: 700; font-size: 40px; letter-spacing: 1px; color: var(--ink);
  }

  .product-title {
    position: absolute; top: 222px; left: 30px; width: 360px; text-align: center;
    font-weight: 700; font-size: 44px; color: var(--title-green); letter-spacing: 0.5px;
  }

  .benefits {
    position: absolute; top: 288px; left: 48px; list-style: none;
    font-size: 15px; line-height: 25px; color: var(--ink);
  }
  .benefits li { display: flex; align-items: center; gap: 5px; }
  .benefits svg { width: 12px; height: 12px; flex: none; }

  .photo { position: absolute; }
  .photo--figure {
    top: 288px; left: 282px; width: 108px; height: 202px;
    background: linear-gradient(160deg, var(--photo-light) 0%, var(--photo-skin) 55%, #d8d8d6 100%);
  }
  .photo--portrait {
    top: 395px; left: 180px; width: 200px; height: 95px;
    background: linear-gradient(180deg, var(--photo-light) 0%, var(--photo-skin) 60%, #c99f82 100%);
  }

  .supplement-band {
    position: absolute; top: 490px; left: 0; width: 100%; height: 46px;
    background: var(--olive); border-bottom: 5px solid var(--band-rule);
    display: flex; align-items: center; justify-content: center;
    font-family: "Open Sans", Arial, sans-serif; font-size: 19px; color: var(--cream);
    letter-spacing: 0.5px;
  }
  .count {
    position: absolute; top: 556px; left: 0; width: 100%; text-align: center;
    font-family: "Open Sans", Arial, sans-serif; font-size: 17px; letter-spacing: 0.5px;
    color: var(--ink);
  }
</style>
</head>
<body>
<main class="canvas">

  <section class="label label--weight">
    <svg class="label__edges" viewBox="0 0 420 650" preserveAspectRatio="none" aria-hidden="true">
      <path d="M0 0 H28 C20 200 20 400 6 650 H0 Z" fill="var(--olive)"/>
      <path d="M28 0 C20 200 20 400 6 650" stroke="var(--lime-edge)" stroke-width="3" fill="none"/>
      <path d="M420 0 H392 C400 200 400 400 414 650 H420 Z" fill="var(--olive)"/>
      <path d="M392 0 C400 200 400 400 414 650" stroke="var(--lime-edge)" stroke-width="3" fill="none"/>
    </svg>
    <div class="maker-name"><span class="maker-name__dot"></span>Bright Meadow Vita</div>
    <div class="product-mark">TIDAL GLOW</div>
    <h2 class="product-title">WEIGHT LOSS</h2>
    <div class="photo photo--figure" role="img" aria-label="Photo of a slim woman measuring her waist with a tape, thumbs up"></div>
    <ul class="benefits">
      <li><svg viewBox="0 0 12 12"><path d="M1 6.5 L4.5 10 L11 2" stroke="var(--title-green)" stroke-width="2" fill="none"/></svg>Reduces fat cells from forming</li>
      <li><svg viewBox="0 0 12 12"><path d="M1 6.5 L4.5 10 L11 2" stroke="var(--title-green)" stroke-width="2" fill="none"/></svg>Increase Weight Loss</li>
      <li><svg viewBox="0 0 12 12"><path d="M1 6.5 L4.5 10 L11 2" stroke="var(--title-green)" stroke-width="2" fill="none"/></svg>Increase Energy levels</li>
      <li><svg viewBox="0 0 12 12"><path d="M1 6.5 L4.5 10 L11 2" stroke="var(--title-green)" stroke-width="2" fill="none"/></svg>Additional Benifits</li>
    </ul>
    <div class="supplement-band">DIETARY SUPPLEMENT</div>
    <div class="count">60 CAPSULES</div>
  </section>

  <section class="label label--hair">
    <svg class="label__edges" viewBox="0 0 420 650" preserveAspectRatio="none" aria-hidden="true">
      <path d="M0 0 H28 C20 200 20 400 6 650 H0 Z" fill="var(--olive)"/>
      <path d="M28 0 C20 200 20 400 6 650" stroke="var(--lime-edge)" stroke-width="3" fill="none"/>
      <path d="M420 0 H392 C400 200 400 400 414 650 H420 Z" fill="var(--olive)"/>
      <path d="M392 0 C400 200 400 400 414 650" stroke="var(--lime-edge)" stroke-width="3" fill="none"/>
    </svg>
    <div class="maker-name"><span class="maker-name__dot"></span>Bright Meadow Vita</div>
    <div class="product-mark">TIDAL GLOW</div>
    <h2 class="product-title">HAIR LOSS</h2>
    <div class="photo photo--portrait" role="img" aria-label="Photo of a balding man with a hairbrush held over his head"></div>
    <ul class="benefits">
      <li><svg viewBox="0 0 12 12"><path d="M1 6.5 L4.5 10 L11 2" stroke="var(--title-green)" stroke-width="2" fill="none"/></svg>Reduces fat cells from forming</li>
      <li><svg viewBox="0 0 12 12"><path d="M1 6.5 L4.5 10 L11 2" stroke="var(--title-green)" stroke-width="2" fill="none"/></svg>Increase Weight Loss</li>
      <li><svg viewBox="0 0 12 12"><path d="M1 6.5 L4.5 10 L11 2" stroke="var(--title-green)" stroke-width="2" fill="none"/></svg>Increase Energy levels</li>
      <li><svg viewBox="0 0 12 12"><path d="M1 6.5 L4.5 10 L11 2" stroke="var(--title-green)" stroke-width="2" fill="none"/></svg>Additional Benifits</li>
    </ul>
    <div class="supplement-band">DIETARY SUPPLEMENT</div>
    <div class="count">60 CAPSULES</div>
  </section>

</main>
</body>
</html>
```